Kelvo Auto - help to get me noticed

We not long ago tasked Pixel Harbour to design a logo for my business. I'm happy with the result so would like to have a business card designed as a follow up.

It's an Automotive service and repair business that offers the following -
- Servicing
- General repairs
- Brakes
- Detailing
- Integrity

Kelvo Automotive
Dallin Mereth
0471 926 317

Target Market(s)

Everyday people with the ability to reach out to corporate customers also.

Industry/Entity Type

Automotive

Contact Information for Business Card

Black card, logo, name and phone number on front. Other details on back of card.

```html
<!DOCTYPE html>
<html lang="en">
<head>
<meta charset="utf-8">
<title>Kelvo Automotive – Business Card</title>
<link rel="stylesheet" href="https://fonts.googleapis.com/css2?family=Saira:wght@700;800&display=swap">
<style>
  :root {
    --bg: #2a2a2a;
    --card: #131417;
    --card-deep: #0e0f11;
    --green: #6cc43a;
    --green-light: #9ed84a;
    --white: #ffffff;
    --faint: #1c1e22;
  }
  * { box-sizing: border-box; margin: 0; padding: 0; }
  html, body { width: 1200px; height: 900px; overflow: hidden; }
  body {
    background: radial-gradient(ellipse at 60% 20%, #3a3a3a 0%, var(--bg) 45%, #151515 100%);
    font-family: "Saira", Arial, sans-serif;
    position: relative;
  }
  .card {
    position: absolute;
    width: 660px;
    height: 377px;
    background: var(--card);
    box-shadow: 0 14px 30px rgba(0,0,0,.55);
    overflow: hidden;
  }
  .card--back { left: 330px; top: 48px; }
  .card--front { left: 210px; top: 476px; }

  .card__band {
    position: absolute; left: 0; right: 0; bottom: 0; height: 7px;
    background: linear-gradient(90deg, var(--white) 0 88%, var(--green) 88% 100%);
  }
  .card__sheen {
    position: absolute; left: 0; right: 0; top: 58px; height: 120px;
    background: linear-gradient(180deg, #25272b 0%, rgba(37,39,43,0) 100%);
  }
  .card__watermark {
    position: absolute; left: 90px; top: 40px;
    font-weight: 800; font-size: 230px; line-height: 1;
    color: var(--faint); letter-spacing: 6px;
  }

  .brand {
    position: absolute;
    color: var(--green);
    font-weight: 800;
    text-transform: uppercase;
    line-height: .95;
  }
  .brand__name { display: block; font-size: 82px; letter-spacing: 2px; }
  .brand__sub { display: block; font-size: 30px; letter-spacing: 4px; }
  .card--back .brand { left: 120px; top: 118px; text-align: right; }
  .card--front .brand { left: 84px; top: 118px; text-align: right; }

  .divider {
    position: absolute; width: 2px; background: var(--white); opacity: .85;
  }
  .card--back .divider { left: 392px; top: 112px; height: 108px; }
  .card--front .divider { left: 362px; top: 126px; height: 122px; }

  .services { position: absolute; left: 418px; top: 112px; list-style: none; }
  .services li {
    display: flex; align-items: center; gap: 12px;
    color: var(--white); font-weight: 700; font-size: 17px;
    letter-spacing: 1.5px; text-transform: uppercase; line-height: 21px;
  }
  .services li::before {
    content: ""; width: 11px; height: 9px; background: var(--green);
  }

  .contact { position: absolute; left: 396px; top: 132px; color: var(--white); }
  .contact__name {
    font-weight: 800; font-size: 31px; letter-spacing: 3px; text-transform: uppercase;
  }
  .contact__phone {
    display: flex; align-items: center; gap: 12px; margin-top: 26px;
    font-weight: 700; font-size: 30px; letter-spacing: 1px;
  }
</style>
</head>
<body>

<section class="card card--back" aria-label="Business card back">
  <div class="card__sheen"></div>
  <div class="card__watermark" aria-hidden="true">KELVO</div>
  <div class="brand">
    <span class="brand__name">Kelvo</span>
    <span class="brand__sub">Automotive</span>
  </div>
  <div class="divider"></div>
  <ul class="services">
    <li>Servicing</li>
    <li>General Repairs</li>
    <li>Brakes</li>
    <li>Detailing</li>
    <li>Integrity</li>
  </ul>
  <div class="card__band"></div>
</section>

<section class="card card--front" aria-label="Business card front">
  <div class="brand">
    <span class="brand__name">Kelvo</span>
    <span class="brand__sub">Automotive</span>
  </div>
  <div class="divider"></div>
  <div class="contact">
    <p class="contact__name">Dallin Mereth</p>
    <p class="contact__phone">
      <svg class="contact__icon" width="26" height="26" viewBox="0 0 26 26" aria-hidden="true">
        <circle cx="13" cy="13" r="11" fill="none" stroke="var(--green)" stroke-width="2"/>
        <path d="M9 8.5c.6-.6 1.3-.5 1.7.1l1 1.5c.3.5.2 1-.2 1.4l-.6.5c.5 1.2 1.5 2.2 2.7 2.7l.5-.6c.4-.4.9-.5 1.4-.2l1.5 1c.6.4.7 1.1.1 1.7l-.7.7c-.9.9-3.4.2-5.6-2s-2.9-4.7-2-5.6z" fill="var(--green)"/>
      </svg>
      0471 926 317
    </p>
  </div>
  <div class="card__band"></div>
</section>

</body>
</html>
```